Security and Staff Identity Business Products Brochure is required.

Looking for a brochure that introduces the business, and the general products and categories we sell.

The flyer will be 2 sided A3 in size, which will be folded in half once printed to effectively be 4 printed sides. 420 x 297mm

I have a lumen-crate account - if there is images you would like to use and i like the design i can purchase them.

As the finalised contact details have not yet available, please ensure that the final contact design can be edited for contact details - Phone, address, email etc.

Content is in the attached files. Ideally the front page will have logo, image/s, and our 3x Value pillars "Global Brands", "Local Supply", "Expert Advice".
Inside will have the 4 product lines w/ content and relevant images.

I have attached an similar brochure for the idea - Titles Tavorn Brochure. PLEASE Note i am after a far more sophisticated and professional looking brochure than this.

Target Market(s)

Potential new customers who need to be introduced to who we are and what range of products we supply

Industry/Entity Type

Security

Other font styles liked:
• Calibri

Colors
abd037
ffffff
919191
1b1b1b
474747
9bcb3c

Requirements
Must have
• Must have 4 categories shown on the inside page/s. Printers, Printer Ribbons, Cards & Access, and Accessories.
• Show the supplier logo's we supply.
• Some not necessarily all corresponding images to those categories.
• Text content in the IDbrochure.docx attachment.
• Must be: 2 sided A3 in size, which will be folded in half once printed to effectively be 4 printed sides. 420 x 297mm
• x Value pillars "Global Brands", "Local Supply", "Expert Advice"
• Colours as per business card and logo design attached.
Nice to have
• Nice to have some background images from Lumen Crate or similar. Business people walking through a business environment.
Should not have
• No cartoons

```html
<!DOCTYPE html>
<html lang="en">
<head>
<meta charset="utf-8">
<title>Keystone Crew Brochure Covers</title>
<link rel="stylesheet" href="https://fonts.googleapis.com/css2?family=Open+Sans:wght@400;600;700&display=swap">
<style>
:root{
  --green:#8cb82b;
  --green-light:#abd037;
  --grey:#6f7073;
  --grey-mid:#919191;
  --grey-dark:#474747;
  --ink:#1b1b1b;
  --white:#ffffff;
  --stage:#2a2a2b;
}
*{box-sizing:border-box;margin:0;padding:0}
html,body{width:1200px;height:789px;overflow:hidden;background:var(--stage);font-family:"Open Sans",Calibri,sans-serif}
.spread{position:absolute;left:70px;top:19px;width:1060px;height:750px;display:flex;box-shadow:0 10px 30px rgba(0,0,0,.5)}
.page{position:relative;width:530px;height:750px;overflow:hidden}

/* back cover */
.back{background:var(--grey)}
.back__green{position:absolute;left:70px;top:0;width:400px;height:750px;background:linear-gradient(160deg,var(--green-light),var(--green))}
.back__headline{position:absolute;left:70px;top:80px;width:400px;text-align:center;color:var(--white);line-height:1.15}
.back__headline .line-a{font-size:30px;letter-spacing:2px;font-weight:400}
.back__headline .line-b{font-size:17px;letter-spacing:.5px;color:var(--ink);opacity:.85}
.back__headline .line-c{font-size:30px;font-weight:700;letter-spacing:2px}
.back__emblem{position:absolute;left:110px;top:200px;width:320px;height:320px;border-radius:50%;background:rgba(255,255,255,.1)}
.brand{display:flex;align-items:center;gap:10px;color:var(--white)}
.brand__dot{width:34px;height:34px;border-radius:50%;background:var(--white);flex:none}
.brand__name{font-size:28px;font-weight:600;line-height:1}
.brand__tag{font-size:10px;margin-top:3px}
.back__brand{position:absolute;left:230px;top:545px}
.contact{position:absolute;left:230px;top:610px;width:300px;height:140px;background:var(--grey);color:var(--white);padding:14px 20px}
.contact__title{font-size:17px;margin-bottom:10px}
.contact__row{display:flex;align-items:center;gap:8px;font-size:11px;line-height:1.5}
.contact__row svg{flex:none}
.contact__social{position:absolute;right:18px;top:18px;display:flex;gap:6px}
.contact__social span{width:14px;height:14px;border-radius:50%;background:var(--green-light)}

/* front cover */
.front{background:var(--white)}
.front__brand{position:absolute;left:50px;top:60px}
.front__brand .brand__dot{background:var(--green)}
.front__brand .brand__name{color:var(--green);font-size:36px}
.front__brand .brand__tag{color:var(--grey-dark);font-size:12px}
.front__photo{position:absolute;left:0;top:150px;width:470px;height:420px;background:linear-gradient(180deg,#eef0f1 0%,#d8dcdf 55%,#b9bcbf 100%)}
.front__band{position:absolute;left:470px;top:180px;width:60px;height:570px;background:var(--green)}
.pillars{position:absolute;left:50px;top:565px;width:460px;height:120px;display:flex;background:var(--grey)}
.pillar{flex:1;display:flex;flex-direction:column;align-items:center;justify-content:center;gap:10px;color:var(--white);font-weight:700;font-size:15px;border-right:1px solid rgba(255,255,255,.15)}
.pillar:last-child{border-right:0}
.front__footer{position:absolute;left:0;top:700px;width:470px;height:50px;background:var(--grey-mid);border-top:3px solid #d9d9d9;display:flex;align-items:center;gap:8px;padding-left:70px;color:var(--white);font-size:13px}
</style>
</head>
<body>
<main class="spread">
  <section class="page back">
    <div class="back__green"></div>
    <div class="back__headline">
      <div class="line-a">KEEPING</div>
      <div class="line-b">YOUR PEOPLE AND BUSINESS</div>
      <div class="line-c">SECURE</div>
    </div>
    <div class="back__emblem"></div>
    <div class="brand back__brand">
      <span class="brand__dot"></span>
      <div><div class="brand__name">Keystone Crew</div><div class="brand__tag">Keeping your people and business secure</div></div>
    </div>
    <div class="contact">
      <div class="contact__title">Office Locations:</div>
      <div class="contact__social"><span></span><span></span><span></span><span></span></div>
      <div class="contact__row">
        <svg width="10" height="12" viewBox="0 0 10 12"><path d="M5 0a4 4 0 0 1 4 4c0 3-4 8-4 8S1 7 1 4a4 4 0 0 1 4-4z" fill="var(--green-light)"/></svg>
        <span>Your business address line 1<br>address line 2</span>
      </div>
      <div class="contact__row">
        <svg width="10" height="10" viewBox="0 0 10 10"><path d="M2 0l2 2-1 2 3 3 2-1 2 2-2 2C4 10 0 6 0 2z" fill="var(--green-light)"/></svg>
        <span>(02) 5550 1776</span>
      </div>
      <div class="contact__row">
        <svg width="11" height="8" viewBox="0 0 11 8"><rect x=".5" y=".5" width="10" height="7" fill="none" stroke="var(--green-light)"/><path d="M.5.5l5 4 5-4" fill="none" stroke="var(--green-light)"/></svg>
        <span>hello@keystonecrew.com.au</span>
      </div>
      <div class="contact__row">
        <svg width="10" height="10" viewBox="0 0 10 10"><circle cx="5" cy="5" r="4.5" fill="none" stroke="var(--green-light)"/><path d="M.5 5h9M5 .5c-3 3-3 6 0 9M5 .5c3 3 3 6 0 9" fill="none" stroke="var(--green-light)"/></svg>
        <span>www.keystonecrew.com.au</span>
      </div>
    </div>
  </section>

  <section class="page front">
    <div class="brand front__brand">
      <span class="brand__dot"></span>
      <div><div class="brand__name">Keystone Crew</div><div class="brand__tag">Keeping your people and business secure</div></div>
    </div>
    <div class="front__band"></div>
    <div class="front__photo" role="img" aria-label="Photo of business people in suits walking through a bright office corridor"></div>
    <div class="pillars">
      <div class="pillar">
        <svg width="56" height="62" viewBox="0 0 56 62"><path d="M28 2l24 8v20c0 15-11 25-24 30C15 55 4 45 4 30V10z" fill="none" stroke="var(--green-light)" stroke-width="3"/><circle cx="20" cy="24" r="5" fill="#fff"/><circle cx="36" cy="24" r="5" fill="#fff"/><circle cx="28" cy="22" r="6" fill="#fff"/><path d="M14 40c0-8 28-8 28 0z" fill="#fff"/></svg>
        <span>Expert Advice</span>
      </div>
      <div class="pillar">
        <svg width="56" height="62" viewBox="0 0 56 62"><path d="M28 2l24 8v20c0 15-11 25-24 30C15 55 4 45 4 30V10z" fill="none" stroke="var(--green-light)" stroke-width="3"/><path d="M28 14a9 9 0 0 1 9 9c0 7-9 17-9 17s-9-10-9-17a9 9 0 0 1 9-9z" fill="#fff"/><circle cx="28" cy="23" r="3" fill="var(--grey)"/></svg>
        <span>Local Supply</span>
      </div>
      <div class="pillar">
        <svg width="56" height="62" viewBox="0 0 56 62"><path d="M28 2l24 8v20c0 15-11 25-24 30C15 55 4 45 4 30V10z" fill="none" stroke="var(--green-light)" stroke-width="3"/><g fill="none" stroke="#fff" stroke-width="2"><circle cx="28" cy="27" r="11"/><path d="M17 27h22M28 16c-6 6-6 16 0 22M28 16c6 6 6 16 0 22M19 21h18M19 33h18"/></g></svg>
        <span>Global Brands</span>
      </div>
    </div>
    <div class="front__footer">
      <svg width="12" height="12" viewBox="0 0 10 10"><circle cx="5" cy="5" r="4.5" fill="none" stroke="var(--green-light)"/><path d="M.5 5h9M5 .5c-3 3-3 6 0 9M5 .5c3 3 3 6 0 9" fill="none" stroke="var(--green-light)"/></svg>
      <span>www.keystonecrew.com.au</span>
    </div>
  </section>
</main>
</body>
</html>
```